Harbor of Embers Label Redesign

We need our current label updated and to look more professional than it currently does. We feel the current image quality is too low and difficult to read. We like the theme of the label, but would like more gold on the label and the gold used to be metallic instead of a dull gold. Attached is our current label design and label on the bottle. We need all the information on it for legal labeling purposes, but please feel free to be creative with the layout and design. The message we want to convey is that this is a natural and luxury anti-aging skincare product. We feel our current label conveys natural, but needs to convey high end skincare more. Additionally, we want to see what the label looks like on the amber bottle with the gold lid image we uploaded.
Here are some of the improvements we would like to see:
-The border smaller and metallic (Shiny) gold
-All the gold shiny (Metallic)
-The print larger and clearer making it easier to read
-The label to not look so stretched out
Uploaded is the bottle we will be using, our logo, and the green leaf background. We also uploaded what we re currently using for comparison.
Target Market(s)
age 28+
Industry/Entity Type
beauty, skincare
Requirements
Must have
- Label information, metallic gold, easy to read

```html
<!DOCTYPE html>
<html lang="en">
<head>
<meta charset="utf-8">
<title>Harbor of Embers – Aging Defense Serum Label</title>
<link href="https://fonts.googleapis.com/css2?family=Cinzel:wght@700&family=Lato:ital,wght@0,400;0,700;1,700&display=swap" rel="stylesheet">
<style>
  :root {
    --page-bg: #d6d6d6;
    --leaf-light: #eaf6cf;
    --leaf-mid: #b9e08a;
    --leaf-deep: #4f9a3a;
    --water: #6fae4f;
    --gold-dark: #a97a16;
    --gold-mid: #d9a933;
    --gold-light: #fde9a3;
    --gold-shine: linear-gradient(180deg, #f9df8a 0%, #d49a1e 45%, #b7800f 60%, #f2cf6b 100%);
    --gold-band: linear-gradient(90deg, #d9a73a 0%, #fbe39a 35%, #f7d77a 60%, #d4a136 100%);
    --ink: #5b430c;
    --brand-green: #1f7a3a;
  }
  * { box-sizing: border-box; margin: 0; padding: 0; }
  html, body { width: 1078px; height: 1200px; overflow: hidden; }
  body { background: var(--page-bg); position: relative; font-family: "Lato", sans-serif; }

  .label {
    position: absolute; left: 39px; top: 347px;
    width: 1000px; height: 505px; border-radius: 18px; overflow: hidden;
    box-shadow: 0 6px 14px rgba(0,0,0,0.25);
  }
  .label-backdrop {
    position: absolute; inset: 0;
    background:
      radial-gradient(ellipse 30% 14% at 25% 86%, rgba(79,154,58,0.55), transparent 70%),
      radial-gradient(ellipse 40% 20% at 75% 88%, rgba(111,174,79,0.35), transparent 70%),
      radial-gradient(ellipse 25% 35% at 2% 30%, rgba(79,154,58,0.45), transparent 70%),
      radial-gradient(ellipse 20% 30% at 99% 20%, rgba(79,154,58,0.4), transparent 70%),
      linear-gradient(180deg, var(--leaf-light) 0%, #d7efb0 45%, var(--leaf-mid) 75%, var(--water) 100%);
  }
  .label-frame {
    position: absolute; inset: 14px 20px; border: 2px solid var(--gold-mid); border-radius: 14px;
  }
  .gold-band {
    position: absolute; top: 14px; bottom: 14px; left: 470px; width: 62px;
    background: var(--gold-band);
    display: flex; align-items: center; justify-content: center;
  }
  .gold-band p {
    writing-mode: vertical-rl; transform: rotate(180deg);
    color: var(--ink); font-size: 13.5px; line-height: 17px; text-align: center; font-weight: 700;
  }
  .gold-band p span { font-weight: 400; }

  .front-panel { position: absolute; left: 20px; top: 0; width: 450px; height: 100%; text-align: center; }
  .brand { position: absolute; top: 50px; left: 0; right: 0; display: flex; align-items: center; justify-content: center; gap: 12px; }
  .brand-dot { width: 50px; height: 50px; border-radius: 50%; background: var(--brand-green); }
  .brand-name { font-family: "Lato", sans-serif; font-weight: 400; font-size: 30px; color: var(--gold-dark); letter-spacing: 2px; }

  .product-title {
    position: absolute; top: 148px; left: 0; right: 0;
    font-family: "Cinzel", serif; font-weight: 700; font-size: 52px; line-height: 50px;
    background: var(--gold-shine); -webkit-background-clip: text; background-clip: text; color: transparent;
  }
  .product-type { position: absolute; top: 322px; left: 0; right: 0; font-style: italic; font-weight: 700; font-size: 22px; color: var(--gold-mid); }
  .key-actives { position: absolute; top: 358px; left: 0; right: 0; font-weight: 700; font-size: 13px; color: var(--ink); }
  .ripple {
    position: absolute; top: 385px; left: 90px; width: 270px; height: 70px; border-radius: 50%;
    background: radial-gradient(ellipse at center, rgba(233,248,206,0.55) 0%, rgba(79,154,58,0.35) 45%, transparent 72%);
  }
  .net-weight {
    position: absolute; bottom: 14px; left: 114px; width: 232px; height: 30px;
    border-radius: 16px 16px 0 0; background: var(--gold-band);
    font-style: italic; font-weight: 700; font-size: 15px; line-height: 30px; color: var(--ink);
  }

  .info-panel { position: absolute; left: 569px; top: 52px; width: 395px; color: var(--ink); font-size: 14.6px; line-height: 17.8px; }
  .info-panel h3 { font-size: 15px; font-weight: 700; }
  .info-panel section + section { margin-top: 14px; }
</style>
</head>
<body>
  <article class="label">
    <div class="label-backdrop" role="img" aria-label="Soft green leaf background with a water ripple"></div>
    <div class="label-frame"></div>

    <div class="front-panel">
      <div class="brand"><span class="brand-dot"></span><span class="brand-name">VERELLE BOTANICS</span></div>
      <h1 class="product-title">HARBOR<br>OF<br>EMBERS</h1>
      <p class="product-type">Aging Defense Serum</p>
      <p class="key-actives">Swiss Apple Stem Cells, Hyaluronic Acid, Retinol, Vitamin E</p>
      <div class="ripple" role="img" aria-label="Water droplet ripple"></div>
      <p class="net-weight">Net Wt: 1 oz/30 mL</p>
    </div>

    <div class="gold-band"><p>MADE IN U.S.A.<br><span>Certified Organic and Natural Ingredients</span></p></div>

    <div class="info-panel">
      <section>
        <h3>Ingredients:</h3>
        <p>Distilled Water, Organic Grape Seed Oil, Organic Jojoba Oil, Organic Avocado Oil, Organic Sunflower Oil, Tocopheryl Acetate (Vitamin E), CellVira™ Malus Domestica (Apple Stem Cell Extract), Hyaluronic Acid, Vitamin A (Retinol), Propylene Glycol, Essential Oil Blend (Tangerine, Lavender, Rosemary), Ethylhexylglycerine, Phenoxyethanol</p>
      </section>
      <section>
        <h3>Directions:</h3>
        <p>Shake bottle prior to use as some separation may naturally occur. Apply generously to face, neck and back of hands morning/night. Can apply under make-up.</p>
      </section>
      <section>
        <h3>WARNINGS:</h3>
        <p>Keep out of eyes. External use only. Discontinue use if irritation occurs. Not intended for children. Consult with a Physician if pregnant, nursing or planning to become pregnant.</p>
      </section>
      <section>
        <h3>Manufactured and Distributed by Verelle Botanics</h3>
        <p>P.O. Box 4820, Lakeview, CO. 80100<br>www.VerelleBotanics.com</p>
      </section>
    </div>
  </article>
</body>
</html>
```